Brightfold Business Card

I would like to re-design my company business card. I have my main company logo (Brightfold) which must remain unchanged and I also have a number of product brands which I would like to also show on the card in some way. The corporate company colors are Blue and Orange, see pantone colors on file. However, it is not necessary to use these colors thoroughout. I am ok with grey tones etc...

Target Market(s)

Trade Business

Industry/Entity Type

Furniture

Contact Information for Business Card

Needs to incorporate Brightfold as the main Logo. The Korvel and Trinable product brands within the company. These can be on the back of the card.

Font styles to use
Sans Serif

Colors
0355a3
f37122

Requirements
Must have
• Marco Feltrani
• COO (Global)
• Brightfold Central Holdings Inc. (4731)
• Level 5, 41 Harlow Street, Melbourne VIC 3000 Australia
• Tel: +61 3 9284 1726 Mobile: +61 427 508 264
• e-mail: marco@brightfold-au.example
• web: www.brightfold-au.example
Nice to have
• Should be a corporate
Should not have
• No images of furniture

```html
<!DOCTYPE html>
<html lang="en">
<head>
<meta charset="utf-8">
<title>Brightfold Business Card</title>
<link href="https://fonts.googleapis.com/css2?family=Arimo:wght@400;700&display=swap" rel="stylesheet">
<style>
  :root {
    --brand-blue: #0355a3;
    --brand-orange: #f37122;
    --card-white: #f6f6f6;
    --ink-white: #ffffff;
    --stage: #2b2b2b;
  }
  * { margin: 0; padding: 0; box-sizing: border-box; }
  html, body {
    width: 1200px; height: 997px; overflow: hidden;
    background: var(--stage);
    font-family: "Arimo", Arial, sans-serif;
  }
  .card {
    position: absolute; left: 280px;
    width: 640px; height: 366px;
    border-radius: 22px; overflow: hidden;
    box-shadow: 0 10px 30px rgba(0,0,0,.45);
  }

  /* Back of card */
  .card-back { top: 80px; background: var(--brand-blue); }
  .card-back .back-lines { position: absolute; inset: 0; }
  .card-back .wordmark {
    position: absolute; left: 150px; top: 140px;
    display: flex; align-items: center; gap: 18px;
  }
  .mark-square {
    width: 60px; height: 60px; border-radius: 10px;
    background: var(--brand-orange);
  }
  .card-back .wordmark-text {
    color: var(--ink-white); font-weight: 700; font-size: 62px; letter-spacing: -1px;
  }
  .product-tabs {
    position: absolute; right: 0; top: 232px;
    display: flex; gap: 8px;
  }
  .product-tab {
    height: 50px; padding: 0 22px; background: var(--ink-white);
    display: flex; align-items: center; justify-content: center;
    color: var(--brand-blue); font-weight: 700; font-size: 24px; letter-spacing: 1px;
  }

  /* Front of card */
  .card-front {
    top: 540px;
    background: linear-gradient(to right,
      var(--card-white) 0 290px,
      var(--brand-blue) 290px 302px,
      var(--card-white) 302px 312px,
      var(--brand-blue) 312px 320px,
      var(--card-white) 320px 330px,
      var(--brand-blue) 330px 100%);
  }
  .front-logo {
    position: absolute; left: 0; width: 290px; top: 70px;
    display: flex; flex-direction: column; align-items: center;
  }
  .front-logo .mark-square { width: 110px; height: 110px; border-radius: 16px; }
  .front-logo .wordmark-text {
    margin-top: 18px; color: var(--brand-blue);
    font-weight: 700; font-size: 52px; letter-spacing: -1px;
  }
  .front-logo .web {
    margin-top: 14px; color: var(--brand-orange);
    font-weight: 700; font-size: 15px; letter-spacing: 1px;
  }
  .contact {
    position: absolute; left: 350px; top: 50px; right: 12px;
    color: var(--ink-white);
  }
  .contact .name { font-weight: 700; font-size: 17px; letter-spacing: .5px; }
  .contact .role { color: var(--brand-orange); font-size: 14px; margin-top: 3px; }
  .contact-list { list-style: none; margin-top: 30px; }
  .contact-list li {
    display: flex; align-items: center; gap: 12px;
    font-size: 14px; margin-bottom: 9px;
  }
  .contact-icon { flex: 0 0 20px; width: 20px; height: 20px; }
  .company {
    color: var(--brand-orange); font-weight: 700; font-size: 12px;
    margin-top: 22px; white-space: nowrap;
  }
  .address { font-size: 14px; line-height: 1.45; margin-top: 6px; }
</style>
</head>
<body>

<section class="card card-back" aria-label="Card back">
  <svg class="back-lines" width="640" height="366" viewBox="0 0 640 366" aria-hidden="true">
    <line x1="0" y1="330" x2="640" y2="236" stroke="#ffffff" stroke-width="3"/>
    <line x1="0" y1="346" x2="640" y2="252" stroke="#ffffff" stroke-width="3"/>
  </svg>
  <div class="wordmark">
    <span class="mark-square"></span>
    <span class="wordmark-text">Brightfold</span>
  </div>
  <div class="product-tabs">
    <span class="product-tab">Korvel</span>
    <span class="product-tab">Trinable</span>
  </div>
</section>

<section class="card card-front" aria-label="Card front">
  <div class="front-logo">
    <span class="mark-square"></span>
    <span class="wordmark-text">Brightfold</span>
    <span class="web">www.brightfold-au.example</span>
  </div>
  <div class="contact">
    <p class="name">MARCO FELTRANI</p>
    <p class="role">COO (GLOBAL)</p>
    <ul class="contact-list">
      <li>
        <svg class="contact-icon" viewBox="0 0 20 20" aria-hidden="true"><circle cx="10" cy="10" r="10" fill="#f37122"/><path d="M6 8c0-1 1-2 2-2l1 2-1 1c.5 1.2 1.5 2.2 2.7 2.7l1-1 2 1c0 1-1 2-2 2-3 0-5.7-2.7-5.7-5.7z" fill="#fff"/></svg>
        +61 3 9284 1726
      </li>
      <li>
        <svg class="contact-icon" viewBox="0 0 20 20" aria-hidden="true"><circle cx="10" cy="10" r="10" fill="#f37122"/><rect x="7" y="4.5" width="6" height="11" rx="1.2" fill="#fff"/></svg>
        +61 427 508 264
      </li>
      <li>
        <svg class="contact-icon" viewBox="0 0 20 20" aria-hidden="true"><circle cx="10" cy="10" r="10" fill="#f37122"/><rect x="5" y="6.5" width="10" height="7" fill="#fff"/><path d="M5 6.5l5 4 5-4" fill="none" stroke="#f37122" stroke-width="1"/></svg>
        marco@brightfold-au.example
      </li>
    </ul>
    <p class="company">Brightfold Central Holdings Inc. (4731)</p>
    <p class="address">Level 5, 41 Harlow Street<br>Melbourne VIC 3000 Australia</p>
  </div>
</section>

</body>
</html>
```